Painted Lanterns- Ever think you'd get a second chance. Ever think you'd get two...

The story is about a woman, mid-40's who gave up on her dreams and her love because of jealousy. Now, 20 years later, she is now a restaurant owner in her little town, but never stops thinking about what she gave up. When a movie project comes to town, she is given a second chance at both. Will she take them?

Target Market(s)

Women 35 to 60

Industry/Entity Type

Entertainment Industry

Font styles to use
Serif
Script

Requirements
Must have
• Deeply feminine...But not overly patronizing.
Nice to have
• Flowery feel.
Should not have
• Dark colors. Sadness.

```html
<!DOCTYPE html>
<html lang="en">
<head>
<meta charset="utf-8">
<title>Painted Lanterns – Film Poster</title>
<link rel="stylesheet" href="https://fonts.googleapis.com/css2?family=Cinzel:wght@400;500&family=Great+Vibes&family=Montserrat:wght@500&family=Oswald:wght@300;600&display=swap">
<style>
  :root {
    --blush: #f8e6e4;
    --window: #fdf3f0;
    --rose: #e07a8f;
    --rose-soft: #ea98a8;
    --plum: #7a4563;
    --white: #ffffff;
    --photo-cool: #6f8fb8;
    --photo-mid: #9aa9c9;
    --photo-warm: #d9b39b;
  }
  html, body { margin: 0; padding: 0; overflow: hidden; background: var(--blush); }
  .poster {
    position: relative;
    width: 896px;
    height: 1200px;
    overflow: hidden;
    background: var(--blush);
    color: var(--plum);
  }
  .poster__shapes { position: absolute; inset: 0; width: 896px; height: 1200px; }
  .studios {
    position: absolute;
    left: 41px;
    top: 282px;
    margin: 0;
    font-family: "Oswald", sans-serif;
    font-weight: 600;
    font-size: 44px;
    line-height: 55px;
    letter-spacing: -0.3px;
    color: var(--plum);
  }
  .studios__line { display: block; }
  .studios__light { font-weight: 300; font-size: 26px; letter-spacing: 0; }
  .studios__line--light { line-height: 46px; }
  .presents {
    position: absolute;
    left: 44px;
    top: 588px;
    margin: 0;
    font-family: "Great Vibes", cursive;
    font-size: 60px;
    line-height: 70px;
    font-weight: 400;
    color: var(--white);
  }
  .title {
    position: absolute;
    left: 40px;
    top: 656px;
    margin: 0;
    font-family: "Cinzel", serif;
    font-weight: 500;
    font-size: 118px;
    line-height: 130px;
    letter-spacing: 2px;
    color: var(--white);
  }
  .title__line { display: block; }
  .cast {
    position: absolute;
    top: 932px;
    margin: 0;
    padding: 0;
    list-style: none;
    font-family: "Montserrat", sans-serif;
    font-weight: 500;
    font-size: 18px;
    line-height: 27px;
    color: var(--white);
  }
  .cast li::before { content: "•"; font-size: 12px; margin-right: 14px; vertical-align: 3px; }
  .cast--left { left: 292px; }
  .cast--right { left: 596px; }
  .credit {
    position: absolute;
    width: 320px;
    margin: 0;
    text-align: center;
    font-family: "Cinzel", serif;
    color: var(--plum);
  }
  .credit__role { display: block; font-size: 10px; letter-spacing: 0.6px; line-height: 14px; }
  .credit__name { display: block; font-size: 21px; line-height: 28px; letter-spacing: 0.5px; }
  .credit--editor { left: -1px; top: 1074px; }
  .credit--costume { left: 292px; top: 1074px; }
  .credit--score { left: 581px; top: 1074px; }
  .credit--photography { left: 208px; top: 1136px; width: 480px; }
</style>
</head>
<body>
<main class="poster">
  <svg class="poster__shapes" viewBox="0 0 694 983" preserveAspectRatio="none">
    <defs>
      <linearGradient id="roseField" x1="0" y1="0" x2="0" y2="1">
        <stop offset="0" stop-color="var(--rose-soft)"/>
        <stop offset="1" stop-color="var(--rose)"/>
      </linearGradient>
      <linearGradient id="couplePhotoTone" x1="0" y1="0" x2="1" y2="1">
        <stop offset="0" stop-color="var(--photo-cool)"/>
        <stop offset="0.55" stop-color="var(--photo-mid)"/>
        <stop offset="1" stop-color="var(--photo-warm)"/>
      </linearGradient>
      <linearGradient id="womanPhotoTone" x1="0" y1="0" x2="0" y2="1">
        <stop offset="0" stop-color="#c99a86"/>
        <stop offset="1" stop-color="#9aa9c9"/>
      </linearGradient>
    </defs>
    <polygon class="rose-field" fill="url(#roseField)"
      points="0,477 300,462 300,260 524,0 694,0 694,849 211,849 51,780 0,795"/>
    <polygon class="frame-window" fill="var(--window)"
      points="322,268 546,28 668,28 668,440 322,462"/>
    <path class="couple-photo" role="img" aria-label="Photo of the lead couple: a man in a blue shirt looking down beside a smiling woman"
      fill="url(#couplePhotoTone)"
      d="M330,120 C340,60 420,30 470,50 C520,80 520,150 560,150 C640,150 670,250 670,330 L672,520 L420,522 L330,520 Z"/>
    <path class="woman-photo" role="img" aria-label="Photo of the lead actress standing, hand at her chin, thinking"
      fill="url(#womanPhotoTone)"
      d="M95,30 C110,15 140,20 145,40 C150,70 160,90 175,110 C190,140 190,180 180,225 L60,225 C55,180 60,140 75,110 C88,85 85,50 95,30 Z"/>
  </svg>

  <h2 class="studios">
    <span class="studios__line">MARIGOLD FILMS <span class="studios__light">AND</span></span>
    <span class="studios__line">BRIGHT MEADOW</span>
    <span class="studios__line">NEW PRODUCTIONS</span>
    <span class="studios__line studios__line--light"><span class="studios__light">IN ASSOCIATION WITH</span></span>
    <span class="studios__line">KESTREL MEDIA</span>
  </h2>

  <p class="presents">Presents</p>
  <h1 class="title">
    <span class="title__line">PAINTED</span>
    <span class="title__line">LANTERNS</span>
  </h1>

  <ul class="cast cast--left">
    <li>NORA WHITFIELD</li>
    <li>DELBERT ASHCOMBE</li>
    <li>SAM VARELA</li>
  </ul>
  <ul class="cast cast--right">
    <li>PETER LINDQVIST</li>
    <li>OWEN CALLISTER</li>
    <li>LENA MAROVIC</li>
  </ul>

  <p class="credit credit--editor"><span class="credit__role">EDITED BY</span><span class="credit__name">EVAN HOLLOWAY</span></p>
  <p class="credit credit--costume"><span class="credit__role">COSTUME DESIGNER</span><span class="credit__name">CLARA BENEDETTI</span></p>
  <p class="credit credit--score"><span class="credit__role">ORIGINAL SCORE BY</span><span class="credit__name">MILES HARTLEY</span></p>
  <p class="credit credit--photography"><span class="credit__role">DIRECTORS OF PHOTOGRAPHY</span><span class="credit__name">GRANT PELLHAM TOBIAS RENNER</span></p>
</main>
</body>
</html>
```